Bookkeeping website design

We need a basic site design for wordpress.
We are a bookkeeping business and will need to present a look consistent with the colours and style of the logo.

Target Market(s)

Business owners

Industry/Entity Type

Accounting/Bookkeeping

Coding

Coded - Design and coding required

Number of Pages Required

1 page

```html
<!DOCTYPE html>
<html lang="en">
<head>
<meta charset="utf-8">
<title>Ledgerline Bookkeeping</title>
<link href="https://fonts.googleapis.com/css2?family=Merriweather:wght@700;900&family=Nunito+Sans:wght@400;600;700;800&display=swap" rel="stylesheet">
<style>
:root{
  --green:#8cc63f;
  --blue:#0a74bd;
  --btn-blue:#1b9be8;
  --cyan:#00b6d6;
  --ink:#111;
  --body:#333;
  --field:#e3e3e3;
  --navy:#0f2a49;
  --copy:#0d8fe0;
  --quote:#cfe6fb;
}
*{box-sizing:border-box;margin:0;padding:0}
html,body{width:1200px;height:3276px;overflow:hidden;background:#fff}
body{position:relative;font-family:"Nunito Sans",sans-serif;color:var(--body)}
.abs{position:absolute}
.serif{font-family:"Merriweather",serif;font-weight:700;color:var(--ink)}
.eyebrow{font-size:12px;color:var(--green);text-transform:uppercase;letter-spacing:.2px}
.btn{position:absolute;display:flex;align-items:center;justify-content:center;color:#fff;font-size:11px;font-weight:700;text-transform:uppercase}
.brand{font-family:"Nunito Sans",sans-serif;font-weight:800;color:var(--blue);font-size:30px;display:flex;align-items:center;gap:8px}
.brand i{display:block;width:22px;height:22px;background:var(--green)}
/* header */
.topbar{left:804px;top:9px;width:396px;height:33px;background:var(--green);border-radius:17px 0 0 17px;color:#fff;font-size:13px;display:flex;align-items:center;padding-left:6px;gap:12px}
.topbar .ph{width:24px;height:24px;border-radius:50%;background:#fff;display:flex;align-items:center;justify-content:center}
.topbar .soc{width:12px;height:12px;border:1.5px solid #fff;border-radius:50%}
.nav a{position:absolute;top:58px;font-size:12px;color:#222;text-decoration:none;font-weight:600}
.nav a.on{color:var(--btn-blue)}
/* hero */
.hero{left:0;top:85px;width:1200px;height:481px;background:linear-gradient(110deg,#6b5a45 0%,#9a8a78 35%,#7d8ea8 60%,#b7bac2 100%);clip-path:polygon(0 0,100% 0,100% 402px,760px 481px,0 405px)}
.hero h1{position:absolute;left:130px;top:70px;font-size:60px;line-height:64px;color:#fff}
.hero p{position:absolute;left:130px;top:280px;font-size:15px;color:#fff}
.dots{left:1129px;top:308px}
.dots span{display:block;width:8px;height:8px;border-radius:50%;background:#fff;margin-bottom:6px}
.dots span:first-child{background:var(--green)}
/* callback */
.callback{left:130px;top:632px;width:300px;height:380px;background:#fff;box-shadow:0 0 10px rgba(0,0,0,.12);padding:27px 26px}
.callback h3{font-size:20px;margin-top:4px;margin-bottom:15px}
.field{background:var(--field);height:33px;font-size:10px;color:#333;padding:10px 11px;margin-bottom:14px}
.field.tall{height:74px}
.intro h2{font-size:30px;line-height:42px}
.intro p{font-size:13px;line-height:19px;width:540px}
.checks{left:509px;top:868px;width:500px;display:grid;grid-template-columns:240px 240px;row-gap:18px;font-size:11px;font-weight:700;color:#222}
.checks div{display:flex;align-items:center;gap:3px;height:15px}
/* features */
.feat{top:1075px;width:300px}
.feat .icon{position:absolute;left:0;top:2px;width:40px;height:46px;background:var(--green);border-radius:8px;opacity:.85}
.feat h4{margin-left:70px;font-size:21px}
.feat p{margin-left:70px;margin-top:12px;font-size:12px;line-height:19px;width:222px}
/* plans */
.plans{left:0;top:1234px;width:770px;height:386px;background:var(--blue)}
.plans .eyebrow{position:absolute;left:130px;top:50px}
.plans h2{position:absolute;left:130px;top:66px;font-size:32px;line-height:36px;color:#fff}
.plans p{position:absolute;left:130px;top:165px;width:460px;font-size:14.5px;line-height:21.5px;color:#fff}
.photo-back{left:609px;top:1290px;width:381px;height:270px;background:linear-gradient(120deg,#8a7563,#3d3936)}
.photo-front{left:782px;top:1318px;width:280px;height:206px;background:#fff;padding:8px}
.photo-front div{width:100%;height:100%;background:linear-gradient(135deg,#e9eef5,#8ea6c7 60%,#2f3c55)}
/* benefits */
.center{left:0;width:1200px;text-align:center}
.benefit{top:1817px;width:230px;text-align:center}
.benefit .art{margin:0 auto;width:86px;height:98px;background:linear-gradient(160deg,#2fc9f2,#0aa7e0);border-radius:10px;transform:skewX(-8deg)}
.benefit h5{margin-top:32px;font-family:"Merriweather",serif;font-size:16px;color:var(--ink)}
.benefit h5 span{color:var(--cyan)}
.benefit p{margin-top:14px;font-size:12px;line-height:18px}
/* team */
.team{left:0;top:2088px;width:1200px;height:465px;background:linear-gradient(180deg,#00b5d4,#0a72b8)}
.team h2{position:absolute;left:0;top:50px;width:1200px;text-align:center;font-size:30px;color:#fff}
.member{top:2206px;width:230px;text-align:center;color:#fff}
.member .ring{position:relative;width:220px;height:220px;margin:0 auto}
.member .pic{position:absolute;left:25px;top:25px;width:170px;height:170px;border-radius:50%;background:linear-gradient(160deg,#cdd3d9,#5a6470)}
.member h6{margin-top:16px;font-family:"Merriweather",serif;font-size:15px}
.member p{margin-top:10px;font-size:12px;line-height:18px}
/* testimonials */
.tcard{top:2713px;width:459px;height:214px;background:#fff;box-shadow:0 0 10px rgba(0,0,0,.1);text-align:center}
.tcard .q1,.tcard .q2{position:absolute;font-family:"Merriweather",serif;font-size:80px;line-height:80px;color:var(--quote)}
.tcard .q1{left:8px;top:-4px}
.tcard .q2{right:8px;bottom:-38px}
.tcard p{margin:62px auto 0;width:400px;font-size:15px;line-height:21px;color:#222}
.tcard b{display:block;margin-top:22px;font-size:12px;color:#111}
.avatar{width:78px;height:78px;border-radius:50%}
/* footer */
.footer{left:0;top:2995px;width:1200px;height:247px;background:var(--navy);color:#fff}
.footer h4{position:absolute;top:54px;font-family:"Merriweather",serif;font-size:15px;color:#fff}
.footer .item{position:absolute;font-size:11.5px;line-height:16px;display:flex;gap:4px}
.fsoc{position:absolute;top:141px;width:30px;height:30px;border:1px solid #fff;border-radius:50%}
.news{position:absolute;left:770px;top:138px;width:300px;height:32px;background:#fff;border-radius:16px;font-size:9px;color:#333;padding:11px 18px}
.news span{position:absolute;right:4px;top:4px;width:24px;height:24px;border-radius:50%;background:var(--btn-blue);display:flex;align-items:center;justify-content:center}
.copyright{left:0;top:3242px;width:1200px;height:34px;background:var(--copy);color:#cfe9ff;font-size:10px;text-align:center;line-height:34px}
.copyright b{color:#fff;font-weight:400}
</style>
</head>
<body>

<!-- header -->
<div class="abs brand" style="left:130px;top:22px">Ledgerline<i></i></div>
<div class="abs topbar">
  <span class="ph"><svg width="12" height="12" viewBox="0 0 24 24"><path d="M6.6 10.8c1.4 2.8 3.8 5.1 6.6 6.6l2.2-2.2c.3-.3.7-.4 1-.2 1.1.4 2.3.6 3.6.6.6 0 1 .4 1 1V20c0 .6-.4 1-1 1C10.6 21 3 13.4 3 4c0-.6.4-1 1-1h3.5c.6 0 1 .4 1 1 0 1.3.2 2.5.6 3.6.1.3 0 .7-.2 1z" fill="#333"/></svg></span>
  <span>+2 (555) 240 6100</span>
  <span style="width:60px"></span>
  <span class="soc" aria-label="social link"></span>
  <span class="soc" aria-label="social link"></span>
  <span class="soc" aria-label="social link"></span>
</div>
<nav class="nav">
  <a class="on" style="left:691px">HOME</a>
  <a style="left:780px">ABOUT US</a>
  <a style="left:893px">SERVICE</a>
  <a style="left:994px">CONTACT US</a>
</nav>

<!-- hero -->
<section class="abs hero" role="img" aria-label="Photo of a professional working on a calculator at a desk">
  <h1 class="serif" style="color:#fff">For<br>Accounting<br>Proffesional</h1>
  <p>There are many variations of passages of Lorem available...</p>
  <span class="btn" style="left:130px;top:322px;width:98px;height:35px;background:var(--green)">Read More</span>
</section>
<div class="abs dots"><span></span><span></span><span></span></div>

<!-- call back -->
<form class="abs callback">
  <div class="eyebrow">Send a Message</div>
  <h3 class="serif">Request a Call Back</h3>
  <div class="field">Name:</div>
  <div class="field">Email:</div>
  <div class="field">Phone:</div>
  <div class="field tall">Message:</div>
  <span class="btn" style="left:97px;top:316px;width:106px;height:34px;background:var(--btn-blue);font-weight:600">Get a Quote</span>
</form>

<div class="abs intro" style="left:509px;top:660px">
  <div class="eyebrow">Welcome to Ledgerline</div>
  <h2 class="serif" style="margin-top:12px">We Will Provide Best Tax<br>Service For Your Business.</h2>
  <p style="margin-top:22px">Sed ut perspiciatis unde omnis iste natus error sit voluptatem accusantium doloremque laudantium, totam rem aperiam, eaque ipsa quae ab illo inventore veritatis et quasi architecto beatae vitae dicta sunt explicabo.</p>
</div>
<div class="abs checks">
  <div><svg width="12" height="10" viewBox="0 0 12 10"><path d="M1 5l3.5 4L11 1" stroke="#8cc63f" stroke-width="1.8" fill="none"/></svg>Learn from customer feedback</div>
  <div><svg width="12" height="10" viewBox="0 0 12 10"><path d="M1 5l3.5 4L11 1" stroke="#8cc63f" stroke-width="1.8" fill="none"/></svg>Learn from customer feedback</div>
  <div><svg width="12" height="10" viewBox="0 0 12 10"><path d="M1 5l3.5 4L11 1" stroke="#8cc63f" stroke-width="1.8" fill="none"/></svg>Professional Team</div>
  <div><svg width="12" height="10" viewBox="0 0 12 10"><path d="M1 5l3.5 4L11 1" stroke="#8cc63f" stroke-width="1.8" fill="none"/></svg>Professional Team</div>
  <div><svg width="12" height="10" viewBox="0 0 12 10"><path d="M1 5l3.5 4L11 1" stroke="#8cc63f" stroke-width="1.8" fill="none"/></svg>High Savings Potential</div>
  <div><svg width="12" height="10" viewBox="0 0 12 10"><path d="M1 5l3.5 4L11 1" stroke="#8cc63f" stroke-width="1.8" fill="none"/></svg>High Savings Potential</div>
  <div><svg width="12" height="10" viewBox="0 0 12 10"><path d="M1 5l3.5 4L11 1" stroke="#8cc63f" stroke-width="1.8" fill="none"/></svg>24/7 customer support</div>
  <div><svg width="12" height="10" viewBox="0 0 12 10"><path d="M1 5l3.5 4L11 1" stroke="#8cc63f" stroke-width="1.8" fill="none"/></svg>24/7 customer support</div>
</div>

<!-- features -->
<div class="abs feat" style="left:130px"><div class="icon" role="img" aria-label="Advisor illustration"></div><h4 class="serif">Expert Advisor</h4><p>But I must explain to you how all this mistaken idea of denouncing pleasure and praising pain</p></div>
<div class="abs feat" style="left:455px"><div class="icon" role="img" aria-label="Tax consultant illustration"></div><h4 class="serif">Tax Consulting</h4><p>But I must explain to you how all this mistaken idea of denouncing pleasure and praising pain</p></div>
<div class="abs feat" style="left:780px"><div class="icon" role="img" aria-label="Financial planning illustration"></div><h4 class="serif">Financial Planing</h4><p>But I must explain to you how all this mistaken idea of denouncing pleasure and praising pain</p></div>

<!-- plans -->
<section class="abs plans">
  <div class="eyebrow">We Offer</div>
  <h2 class="serif" style="color:#fff">Popular Plans for General<br>Feature</h2>
  <p>On the other hand, we denounce with righteous indignation and dislike men who are so beguiled and demoralized by the charms of pleasure of the moment, so blinded by desire, that they cannot foresee the pain and trouble that are bound to ensue; and equal blame belongs to those who fail in their duty...</p>
  <span class="btn" style="left:130px;top:301px;width:99px;height:35px;background:var(--btn-blue);font-weight:600">Read More</span>
</section>
<div class="abs photo-back" role="img" aria-label="Photo of a smiling businesswoman at a desk"></div>
<div class="abs photo-front"><div role="img" aria-label="Photo of a businessman reviewing charts"></div></div>

<!-- benefits -->
<div class="abs center eyebrow" style="top:1686px">What You</div>
<h2 class="abs center serif" style="top:1708px;font-size:30px">Get With Ledgerline</h2>
<p class="abs center" style="top:1757px;font-size:15px;color:#222">Nam libero tempore, cum soluta nobis est eligendi optio cumque nihil impedit</p>
<div class="abs benefit" style="left:125px"><div class="art" role="img" aria-label="Accounting book illustration"></div><h5><span>Rerum</span> Necessitatibus</h5><p>But in certain circumstances<br>and owing to the claims of duty or the obligations of business</p></div>
<div class="abs benefit" style="left:365px"><div class="art" role="img" aria-label="Calculator illustration"></div><h5><span>Rerum</span> Necessitatibus</h5><p>But in certain circumstances<br>and owing to the claims of duty or the obligations of business</p></div>
<div class="abs benefit" style="left:605px"><div class="art" role="img" aria-label="Invoice illustration"></div><h5><span>Rerum</span> Necessitatibus</h5><p>But in certain circumstances<br>and owing to the claims of duty or the obligations of business</p></div>
<div class="abs benefit" style="left:845px"><div class="art" role="img" aria-label="Financial report illustration"></div><h5><span>Rerum</span> Necessitatibus</h5><p>But in certain circumstances<br>and owing to the claims of duty or the obligations of business</p></div>

<!-- team -->
<section class="abs team"><h2 class="serif">Meet Our Team</h2></section>
<svg width="0" height="0" style="position:absolute"><defs><g id="arcs"><path d="M40 70 A100 100 0 0 1 100 12" stroke="#fff" stroke-width="3" fill="none"/><path d="M120 12 A100 100 0 0 1 180 70" stroke="#fff" stroke-width="3" fill="none"/><path d="M180 150 A100 100 0 0 1 120 208" stroke="#fff" stroke-width="3" fill="none"/><path d="M100 208 A100 100 0 0 1 40 150" stroke="#fff" stroke-width="3" fill="none"/></g></defs></svg>
<div class="abs member" style="left:125px"><div class="ring"><svg width="220" height="220" class="abs" style="left:0;top:0"><use href="#arcs"/></svg><div class="pic" role="img" aria-label="Portrait of team member Maren"></div></div><h6>MAREN</h6><p>But I must explain to you how all this mistaken idea...</p></div>
<div class="abs member" style="left:365px"><div class="ring"><svg width="220" height="220" class="abs" style="left:0;top:0"><use href="#arcs"/></svg><div class="pic" role="img" aria-label="Portrait of team member Oskel"></div></div><h6>OSKEL</h6><p>But I must explain to you how all this mistaken idea...</p></div>
<div class="abs member" style="left:605px"><div class="ring"><svg width="220" height="220" class="abs" style="left:0;top:0"><use href="#arcs"/></svg><div class="pic" role="img" aria-label="Portrait of team member Davina"></div></div><h6>DAVINA</h6><p>But I must explain to you how all this mistaken idea...</p></div>
<div class="abs member" style="left:845px"><div class="ring"><svg width="220" height="220" class="abs" style="left:0;top:0"><use href="#arcs"/></svg><div class="pic" role="img" aria-label="Portrait of team member Thorne" style="background:linear-gradient(160deg,#6a4a3a,#2a1d1a)"></div></div><h6>THORNE</h6><p>But I must explain to you how all this mistaken idea...</p></div>

<!-- testimonials -->
<h2 class="abs center serif" style="top:2612px;font-size:30px">Testimonials</h2>
<div class="abs tcard" style="left:130px"><span class="q1">&ldquo;</span><span class="q2">&rdquo;</span><p>Sed ut perspiciatis unde omnis iste natus error sit voluptatem accusantium doloremque laudantium, totam rem aperiam, eaque ipsa quae ab illo inventore veritatis et quasi architecto beatae vitae dicta sunt explicabo.</p><b>ELENA MARSH</b></div>
<div class="abs tcard" style="left:611px"><span class="q1">&ldquo;</span><span class="q2">&rdquo;</span><p>Sed ut perspiciatis unde omnis iste natus error sit voluptatem accusantium doloremque laudantium, totam rem aperiam, eaque ipsa quae ab illo inventore veritatis et quasi architecto beatae vitae dicta sunt explicabo.</p><b>PETER HOLLOWAY</b></div>
<div class="abs avatar" style="left:321px;top:2672px;background:linear-gradient(160deg,#f0a060,#c8663a)" role="img" aria-label="Portrait of Elena Marsh"></div>
<div class="abs avatar" style="left:801px;top:2672px;background:linear-gradient(160deg,#8594a8,#3b4454)" role="img" aria-label="Portrait of Peter Holloway"></div>

<!-- footer -->
<footer class="abs footer">
  <div class="brand" style="position:absolute;left:134px;top:62px;color:#fff">Ledgerline<i></i></div>
  <span class="fsoc" style="left:130px" aria-label="social link"></span>
  <span class="fsoc" style="left:171px" aria-label="social link"></span>
  <span class="fsoc" style="left:214px" aria-label="social link"></span>
  <h4 style="left:449px">Contact Us</h4>
  <div class="item" style="left:449px;top:90px"><svg width="9" height="12" viewBox="0 0 10 14"><path d="M5 0C2.2 0 0 2.2 0 5c0 3.8 5 9 5 9s5-5.2 5-9c0-2.8-2.2-5-5-5zm0 7a2 2 0 110-4 2 2 0 010 4z" fill="#1b9be8"/></svg><span>48/B Lorem ipsum dolor sit amet<br>Northvale 31KT USA</span></div>
  <div class="item" style="left:449px;top:143px"><svg width="9" height="12" viewBox="0 0 24 24"><path d="M6.6 10.8c1.4 2.8 3.8 5.1 6.6 6.6l2.2-2.2c.3-.3.7-.4 1-.2 1.1.4 2.3.6 3.6.6.6 0 1 .4 1 1V20c0 .6-.4 1-1 1C10.6 21 3 13.4 3 4c0-.6.4-1 1-1h3.5c.6 0 1 .4 1 1 0 1.3.2 2.5.6 3.6.1.3 0 .7-.2 1z" fill="#1b9be8"/></svg><span>+2 (555) 240 6100</span></div>
  <div class="item" style="left:449px;top:184px"><svg width="10" height="12" viewBox="0 0 12 10"><rect x="0" y="1" width="12" height="8" fill="#1b9be8"/><path d="M0 1l6 4 6-4" stroke="#0f2a49" fill="none"/></svg><span>info@ledgerlinebooks.com</span></div>
  <h4 style="left:769px">Newsletter</h4>
  <div class="item" style="left:769px;top:90px;font-size:10px;width:310px">Sed ut perspiciatis unde omnis iste natus error sit voluptatem accusantium doloremque laudantium</div>
  <div class="news">Enter Your Email:<span><svg width="11" height="11" viewBox="0 0 12 12"><path d="M1 6l10-5-3 10-2-4z" fill="#fff"/></svg></span></div>
</footer>
<div class="abs copyright">Copyright &copy; 2021 <b>Ledgerline Bookkeeping</b>. All Rights Reserved.</div>

</body>
</html>
```